Make attractive Packaging label for NUT BUTTERS jars

We at Velvet Orchard are launching our own line of NUT BUTTERS. We will be serving them in GLASS JARS ready packaged. I need attractive luxurious design for glass jar and should be designed ready to print.
I have attached glass jar pictures and measurement sheet.
My company logo has been attached. Also company details can be found on our facebook page.
product will be

ALMOND BUTTER
CASHEW BUTTER
PEANUT BUTTER
HAZELNUT BUTTER.

```html
<!DOCTYPE html>
<html lang="en">
<head>
<meta charset="utf-8">
<title>Velvet Orchard – Nut Butter Labels</title>
<link rel="stylesheet" href="https://fonts.googleapis.com/css2?family=Alfa+Slab+One&family=Oswald:wght@300;400&display=swap">
<style>
  :root {
    --peanut: #e2b425;
    --almond: #b58a55;
    --cashew: #b58a55;
    --hazelnut: #cf6238;
    --ink: #231f20;
    --brand: #6b3e1e;
    --paper: #ffffff;
    --stage: #e4e4e4;
    --title-font: "Alfa Slab One", Georgia, serif;
    --body-font: "Oswald", Arial, sans-serif;
  }
  * { box-sizing: border-box; margin: 0; padding: 0; }
  html, body { width: 920px; height: 1200px; overflow: hidden; }
  body { background: var(--stage); position: relative; font-family: var(--body-font); }

  .brand-name {
    font-family: var(--title-font);
    color: var(--brand);
    text-align: center;
    line-height: 1;
    font-size: 22px;
  }
  .brand-name span { display: block; }

  .badge {
    position: absolute; left: 50%; bottom: 0;
    transform: translateX(-50%);
    width: 58px; height: 30px;
    background: var(--ink);
    border-radius: 29px 29px 0 0;
    color: var(--paper);
    font-size: 8px; line-height: 1.05;
    text-align: center; padding-top: 8px;
    white-space: nowrap;
  }

  /* Rectangular front label */
  .label {
    position: absolute; width: 272px; height: 219px;
    background: var(--paper);
    display: flex; flex-direction: column;
    transform-origin: top left;
  }
  .label--small { transform: scale(.8); }
  .label__head { height: 94px; display: flex; align-items: center; justify-content: center; }
  .label__rule { height: 6px; background: var(--ink); }
  .label__band {
    flex: 1; position: relative;
    display: flex; flex-direction: column; align-items: center;
    padding-top: 24px; color: var(--paper);
  }
  .label__title { font-family: var(--title-font); font-size: 20px; letter-spacing: .5px; white-space: nowrap; }
  .label__sub { font-size: 12px; font-weight: 300; margin-top: 4px; letter-spacing: .3px; white-space: nowrap; }
  .label__foot { height: 10px; background: var(--ink); position: relative; }

  .flavour--peanut { background: var(--peanut); }
  .flavour--almond { background: var(--almond); }
  .flavour--hazelnut { background: var(--hazelnut); }

  /* Round lid label */
  .lid {
    position: absolute; top: 272px; width: 247px; height: 247px;
    border-radius: 50%; overflow: hidden; background: var(--paper);
  }
  .lid__fill { position: absolute; left: 0; right: 0; top: 50%; bottom: 0; }
  .lid__ring { position: absolute; inset: 14px; border: 4px solid var(--ink); border-radius: 50%; }
  .lid__brand { position: absolute; top: 52px; left: 0; right: 0; }
  .lid__text {
    position: absolute; top: 140px; left: 0; right: 0;
    text-align: center; color: var(--paper);
  }
  .lid__title { font-family: var(--title-font); font-size: 15px; line-height: 1.15; }
  .lid__natural { font-size: 9px; font-weight: 300; margin-top: 4px; line-height: 1.1; }

  /* Wrap label with top tab */
  .wrap { position: absolute; top: 925px; width: 212px; height: 204px; }
  .wrap__art { position: absolute; inset: 0; }
  .wrap__tab { position: absolute; left: 88px; top: -38px; width: 36px; height: 120px; background: var(--paper); }
  .wrap__logo {
    position: absolute; left: 62px; top: 56px; width: 88px; height: 88px;
    border-radius: 50%; background: var(--paper);
    display: flex; align-items: center; justify-content: center;
  }
  .wrap__logo .brand-name { font-size: 14px; }
  .wrap__text { position: absolute; left: 0; right: 0; top: 142px; text-align: center; color: var(--ink); }
  .wrap__title { font-family: var(--title-font); font-size: 16px; white-space: nowrap; }
  .wrap__sub { font-size: 10px; font-weight: 300; margin-top: 1px; white-space: nowrap; }
  .wrap__foot { position: absolute; left: 0; right: 0; bottom: 0; height: 8px; background: var(--ink); }
</style>
</head>
<body>

  <!-- Front labels -->
  <section class="label" style="left:23px; top:22px;">
    <div class="label__head"><div class="brand-name"><span>Velvet</span><span>Orchard</span></div></div>
    <div class="label__rule"></div>
    <div class="label__band flavour--peanut" role="img" aria-label="Yellow band with faint peanut outline pattern">
      <div class="label__title">PEANUT BUTTER</div>
      <div class="label__sub">NUTS • DRIED FRUITS • SEEDS</div>
    </div>
    <div class="label__foot"><div class="badge">100%<br>NATURAL</div></div>
  </section>
  <section class="label" style="left:320px; top:22px;">
    <div class="label__head"><div class="brand-name"><span>Velvet</span><span>Orchard</span></div></div>
    <div class="label__rule"></div>
    <div class="label__band flavour--almond" role="img" aria-label="Almond brown band with faint almond outline pattern">
      <div class="label__title">ALMOND BUTTER</div>
      <div class="label__sub">NUTS • DRIED FRUITS • SEEDS</div>
    </div>
    <div class="label__foot"><div class="badge">100%<br>NATURAL</div></div>
  </section>
  <section class="label" style="left:613px; top:22px;">
    <div class="label__head"><div class="brand-name"><span>Velvet</span><span>Orchard</span></div></div>
    <div class="label__rule"></div>
    <div class="label__band flavour--hazelnut" role="img" aria-label="Hazelnut orange band with faint hazelnut outline pattern">
      <div class="label__title">HAZELNUT BUTTER</div>
      <div class="label__sub">NUTS • DRIED FRUITS • SEEDS</div>
    </div>
    <div class="label__foot"><div class="badge">100%<br>NATURAL</div></div>
  </section>

  <!-- Lid labels -->
  <section class="lid" style="left:45px;">
    <div class="lid__fill flavour--peanut" role="img" aria-label="Yellow half with faint peanut outline pattern"></div>
    <div class="lid__ring"></div>
    <div class="lid__brand brand-name"><span>Velvet</span><span>Orchard</span></div>
    <div class="lid__text"><div class="lid__title">PEANUT<br>BUTTER</div><div class="lid__natural">100%<br>NATURAL</div></div>
  </section>
  <section class="lid" style="left:332px;">
    <div class="lid__fill flavour--almond" role="img" aria-label="Almond brown half with faint almond outline pattern"></div>
    <div class="lid__ring"></div>
    <div class="lid__brand brand-name"><span>Velvet</span><span>Orchard</span></div>
    <div class="lid__text"><div class="lid__title">ALMOND<br>BUTTER</div><div class="lid__natural">100%<br>NATURAL</div></div>
  </section>
  <section class="lid" style="left:630px;">
    <div class="lid__fill flavour--hazelnut" role="img" aria-label="Hazelnut orange half with faint hazelnut outline pattern"></div>
    <div class="lid__ring"></div>
    <div class="lid__brand brand-name"><span>Velvet</span><span>Orchard</span></div>
    <div class="lid__text"><div class="lid__title">HAZELNUT<br>BUTTER</div><div class="lid__natural">100%<br>NATURAL</div></div>
  </section>

  <!-- Jar front labels, smaller size -->
  <section class="label label--small" style="left:52px; top:630px;">
    <div class="label__head"><div class="brand-name"><span>Velvet</span><span>Orchard</span></div></div>
    <div class="label__rule"></div>
    <div class="label__band flavour--peanut" role="img" aria-label="Yellow band with faint peanut outline pattern">
      <div class="label__title">PEANUT BUTTER</div>
      <div class="label__sub">NUTS • DRIED FRUITS • SEEDS</div>
    </div>
    <div class="label__foot"><div class="badge">100%<br>NATURAL</div></div>
  </section>
  <section class="label label--small" style="left:349px; top:630px;">
    <div class="label__head"><div class="brand-name"><span>Velvet</span><span>Orchard</span></div></div>
    <div class="label__rule"></div>
    <div class="label__band flavour--almond" role="img" aria-label="Almond brown band with faint almond outline pattern">
      <div class="label__title">ALMOND BUTTER</div>
      <div class="label__sub">NUTS • DRIED FRUITS • SEEDS</div>
    </div>
    <div class="label__foot"><div class="badge">100%<br>NATURAL</div></div>
  </section>
  <section class="label label--small" style="left:645px; top:630px;">
    <div class="label__head"><div class="brand-name"><span>Velvet</span><span>Orchard</span></div></div>
    <div class="label__rule"></div>
    <div class="label__band flavour--hazelnut" role="img" aria-label="Hazelnut orange band with faint hazelnut outline pattern">
      <div class="label__title">HAZELNUT BUTTER</div>
      <div class="label__sub">NUTS • DRIED FRUITS • SEEDS</div>
    </div>
    <div class="label__foot"><div class="badge">100%<br>NATURAL</div></div>
  </section>

  <!-- Wrap labels with tab -->
  <section class="wrap" style="left:57px;">
    <svg class="wrap__art" width="212" height="204" viewBox="0 0 212 204" role="img" aria-label="Yellow top with faint peanut outline pattern curving into white base">
      <rect width="212" height="204" fill="var(--peanut)"/>
      <path d="M0 135 Q106 40 212 135 L212 204 L0 204 Z" fill="var(--paper)"/>
    </svg>
    <div class="wrap__tab"></div>
    <div class="wrap__logo"><div class="brand-name"><span>Velvet</span><span>Orchard</span></div></div>
    <div class="wrap__text"><div class="wrap__title">PEANUT BUTTER</div><div class="wrap__sub">NUTS • DRIED FRUITS • SEEDS</div></div>
    <div class="wrap__foot"></div>
    <div class="badge">100%<br>NATURAL</div>
  </section>
  <section class="wrap" style="left:354px;">
    <svg class="wrap__art" width="212" height="204" viewBox="0 0 212 204" role="img" aria-label="Warm tan top with faint cashew outline pattern curving into white base">
      <rect width="212" height="204" fill="var(--cashew)"/>
      <path d="M0 135 Q106 40 212 135 L212 204 L0 204 Z" fill="var(--paper)"/>
    </svg>
    <div class="wrap__tab"></div>
    <div class="wrap__logo"><div class="brand-name"><span>Velvet</span><span>Orchard</span></div></div>
    <div class="wrap__text"><div class="wrap__title">CASHEW BUTTER</div><div class="wrap__sub">NUTS • DRIED FRUITS • SEEDS</div></div>
    <div class="wrap__foot"></div>
    <div class="badge">100%<br>NATURAL</div>
  </section>
  <section class="wrap" style="left:650px;">
    <svg class="wrap__art" width="212" height="204" viewBox="0 0 212 204" role="img" aria-label="Hazelnut orange top with faint hazelnut outline pattern curving into white base">
      <rect width="212" height="204" fill="var(--hazelnut)"/>
      <path d="M0 135 Q106 40 212 135 L212 204 L0 204 Z" fill="var(--paper)"/>
    </svg>
    <div class="wrap__tab"></div>
    <div class="wrap__logo"><div class="brand-name"><span>Velvet</span><span>Orchard</span></div></div>
    <div class="wrap__text"><div class="wrap__title">HAZELNUT BUTTER</div><div class="wrap__sub">NUTS • DRIED FRUITS • SEEDS</div></div>
    <div class="wrap__foot"></div>
    <div class="badge">100%<br>NATURAL</div>
  </section>

</body>
</html>
```